"Lantern Field" Play - Poster Design for Theatre Group

We are an amateur theatre group based in Geneva, Switzerland. We take pride in eye-catching posters for our shows, which are printed in various sizes.
This design will be for a play in March 2016. The play is called "Lantern Field", and it's a Harwick Medal winner from Morgan Pellew-Strand. The play is about a couple who have everything a family could want, until they lose a child in a life-shattering accident that turns their world upside down. The play charts the couple's bittersweet search to find each other and to find comfort.
Most importantly, we want a design that will make people want to see the show. We don't want to give away the plot or be too heavy-handed about death, but we want it to be clear that it's not a comedy (although there are some lighter moments!).
Attached you will find a template for the poster. This simply has our group name and logo in the top right corner: (Lakeside Stage Players Circle presents).
You may change the color of both the text and the logo, but please do not change the font, size, or location.
Here is the information that needs to be on the poster, wherever you see fit:
play title: Lantern Field
author byline: by Morgan Pellew-Strand
director line: directed by Ned Variscombe
tagline: How do you keep it together when your whole world's fallen apart?
dates and times:
1-5 March 2016
(Tue-Fri 20:00, Sat 19:00)
location:
Théâtre du Vieux Moulin
Rive-Claire, Lacmont
websites:
www.lspc.ch
www.scenesauboulevard.ch
Technical Details:
Any font or combination of fonts is acceptable. The largest text should be the play title. The author's name must be at least 50% of the title font size.
For this competition, we would like the version with A3 proportions, which will also be used at F4 (89.5 x 128 cm) and A5 sizes (14.8 x 21 cm). Therefore no text should be below 9pt at A5.
However, from the winning designer we will also need repurposed sizes of the same design. Here is a comprehensive list of the sizes we will need.
1) A3 print poster. Artwork should be 300dpi, CMYK, sent with a 1mm bleed all round, to specification PDF/X-1A:2001. We will need this image in PDF format in addition to the default Artmarketly formats.
2) Friendora advert picture. 1200px by 628px, RGB jpeg. This must comply with Friendora’s restrictions on amount of text, which is no more than 20% of area taken up by text.(https://www.friendora.example/ads/tools/text_overlay).
Because of these restrictions it is sufficient to include just the title and the author's name in this version.
3) Friendora cover picture: 851px by 314px. RGB jpeg. It is sufficient to include just the title and the author's name in this version.
4) Web banner. 1000px by 300px. RGB jpeg. This version should include just the main image(s), no text.

```html
<!DOCTYPE html>
<html lang="en">
<head>
<meta charset="utf-8">
<title>Lantern Field – Lakeside Stage Players Circle</title>
<link rel="stylesheet" href="https://fonts.googleapis.com/css2?family=Montserrat:wght@300;400;700;800;900&family=Roboto+Condensed:wght@700&family=Cinzel:wght@700&display=swap">
<style>
  :root {
    --paper: #d8d0c3;
    --paper-light: #e3ddd2;
    --ink: #2a2118;
    --ink-soft: #4a3d30;
    --bronze: #8a6a44;
    --bronze-light: #a88a62;
    --torn-edge: #eeeae2;
    --glow: #fff9ec;
    --sepia-mid: #b8955f;
    --sepia-dark: #2b1d10;
    --white: #ffffff;
  }
  * { margin: 0; padding: 0; box-sizing: border-box; }
  html, body { width: 850px; height: 1200px; overflow: hidden; background: var(--paper); }
  .poster {
    position: relative;
    width: 850px; height: 1200px;
    background: radial-gradient(ellipse at 50% 40%, var(--paper-light), var(--paper) 75%);
    font-family: "Montserrat", sans-serif;
    color: var(--ink);
    overflow: hidden;
  }

  /* Presenter block */
  .presenter {
    position: absolute; top: 78px; right: 199px;
    text-align: right;
    font-family: "Roboto Condensed", sans-serif;
    font-weight: 700; font-size: 21px; line-height: 26px;
    color: var(--ink);
  }
  .presenter-mark {
    position: absolute; top: 60px; left: 672px;
    width: 112px; height: 112px; border-radius: 50%;
    background: var(--ink);
  }

  /* Title block */
  .accolade {
    position: absolute; top: 220px; left: 0; width: 850px;
    text-align: center; font-weight: 400; font-size: 14px;
    letter-spacing: 2.4px; color: var(--ink-soft);
  }
  .play-title {
    position: absolute; top: 244px; left: 0; width: 850px;
    text-align: center; font-weight: 900; font-size: 94px;
    line-height: 100px; letter-spacing: -2px;
    transform: scaleY(1.15); transform-origin: 50% 0;
    background: linear-gradient(180deg, var(--ink) 45%, var(--bronze) 100%);
    -webkit-background-clip: text; background-clip: text; color: transparent;
  }
  .author {
    position: absolute; top: 356px; left: 0; width: 850px;
    text-align: center; font-size: 32px; line-height: 40px;
  }
  .author-by { font-weight: 300; color: var(--ink-soft); }
  .author-name {
    font-weight: 800; letter-spacing: 0.5px;
    background: linear-gradient(90deg, var(--ink-soft), var(--bronze), var(--bronze-light));
    -webkit-background-clip: text; background-clip: text; color: transparent;
  }

  /* Image band */
  .image-band {
    position: absolute; top: 430px; left: 0; width: 850px; height: 520px;
    background:
      radial-gradient(circle at 681px 190px, var(--glow) 0, var(--glow) 40px, var(--sepia-mid) 170px, transparent 420px),
      linear-gradient(90deg, var(--sepia-dark) 0%, #5a4126 40%, #8d6c44 70%, #7a5a36 100%);
  }
  .torn-edge { position: absolute; left: 0; width: 850px; height: 24px; }
  .torn-edge--top { top: 424px; }
  .torn-edge--bottom { top: 930px; }
  .tagline {
    position: absolute; top: 648px; left: 121px; width: 280px;
    text-align: center; font-weight: 800; font-size: 17px; line-height: 20px;
    color: var(--white);
  }

  /* Credits and details */
  .director {
    position: absolute; top: 968px; left: 0; width: 850px; text-align: center;
  }
  .director-label { display: block; font-weight: 300; font-size: 17px; line-height: 20px; color: var(--ink-soft); }
  .director-name { display: block; font-weight: 700; font-size: 17px; line-height: 22px; }
  .run-dates {
    position: absolute; top: 1028px; left: 0; width: 850px; text-align: center;
    font-weight: 800; font-size: 41px; line-height: 46px; letter-spacing: -0.5px;
  }
  .showtimes {
    position: absolute; top: 1077px; left: 0; width: 850px; text-align: center;
    font-family: "Cinzel", serif; font-weight: 700; font-size: 16px; line-height: 22px;
  }
  .showtimes .sep { font-family: "Montserrat", sans-serif; font-weight: 300; margin: 0 4px; }

  .footer-item { position: absolute; top: 1128px; text-align: center; font-size: 14px; line-height: 18px; }
  .footer-label { display: block; font-weight: 400; }
  .footer-value { display: block; font-weight: 700; }
  .footer-info { left: 88px; width: 120px; }
  .footer-tickets { left: 580px; width: 240px; }
  .venue {
    position: absolute; top: 1124px; left: 285px; width: 280px; text-align: center;
    font-family: "Cinzel", serif; font-weight: 700; font-size: 18px; line-height: 24px;
  }
  .divider { position: absolute; top: 1127px; width: 2px; height: 36px; background: var(--ink); }
  .divider--left { left: 272px; }
  .divider--right { left: 578px; }
</style>
</head>
<body>
<div class="poster">

  <div class="presenter">Lakeside Stage<br>Players Circle<br>presents</div>
  <div class="presenter-mark"></div>

  <p class="accolade">WINNER OF THE 2007 HARWICK MEDAL FOR DRAMA</p>
  <h1 class="play-title">LANTERN FIELD</h1>
  <p class="author"><span class="author-by">by </span><span class="author-name">MORGAN PELLEW-STRAND</span></p>

  <div class="image-band" role="img" aria-label="Sepia photograph of a couple walking apart out of a glowing tunnel, their shadows stretching toward the viewer"></div>
  <svg class="torn-edge torn-edge--top" viewBox="0 0 850 24" preserveAspectRatio="none">
    <polygon fill="var(--torn-edge)" points="0,0 850,0 850,14 820,10 790,16 760,9 725,15 690,11 655,17 620,10 585,14 550,9 515,16 480,11 445,15 410,10 375,17 340,11 305,15 270,9 235,16 200,12 165,15 130,9 95,16 60,11 30,15 0,10"/>
  </svg>
  <svg class="torn-edge torn-edge--bottom" viewBox="0 0 850 24" preserveAspectRatio="none">
    <polygon fill="var(--torn-edge)" points="0,24 850,24 850,9 815,14 780,8 745,13 710,7 675,14 640,9 605,13 570,6 535,12 500,8 465,14 430,7 395,12 360,9 325,14 290,7 255,13 220,8 185,14 150,9 115,13 80,7 45,12 0,8"/>
  </svg>
  <p class="tagline">How do you<br>keep it together<br>when your whole world<br>has fallen apart?</p>

  <p class="director"><span class="director-label">directed by</span><span class="director-name">NED VARISCOMBE</span></p>
  <p class="run-dates">1 - 5 MARCH 2016</p>
  <p class="showtimes">Tuesday to Friday 20:00<span class="sep">|</span>Saturday 19:00</p>

  <p class="footer-item footer-info"><span class="footer-label">info:</span><span class="footer-value">LSPC.CH</span></p>
  <span class="divider divider--left"></span>
  <p class="venue">Théâtre du Vieux Moulin<br>Rive-Claire, Lacmont</p>
  <span class="divider divider--right"></span>
  <p class="footer-item footer-tickets"><span class="footer-label">tickets:</span><span class="footer-value">SCENESAUBOULEVARD.CH</span></p>

</div>
</body>
</html>
```